Foldable Airlink Headphone Packaging Design

We would like a window box style packaging design for our Foldable Airlink Headphone.

We want to use the packaging for 4-5 of our Airlink headphone series (enclosed picture of the headphones for reference) and hence we would not like to put any product pictures on the packaging.
Material: E-Flute Paper box
Type: Window Box style
Design features we prefer: Colorful, creative, trendy, High tech.
Requirement: AI file is preferred
Size of Packaging: 170 (L) x 120 (W) x 200 (H) mm

Enclosed are a detailed description along with competitor designs for your reference.

Any further questions, please feel free to ask.

Target Market(s)

25-35 year olds

Industry/Entity Type

Electronics

Colors

Designer to choose colors to be used in the design.

Requirements
Must have
• Trendy Design

```html
<!DOCTYPE html>
<html lang="en">
<head>
<meta charset="utf-8">
<title>Foldable Airlink Headphone – Window Box</title>
<link rel="stylesheet" href="https://fonts.googleapis.com/css2?family=Orbitron:wght@800;900&family=Montserrat:wght@300;700&display=swap">
<style>
  :root {
    --backdrop: #e4e4e6;
    --cyan: #3cc4ef;
    --cyan-light: #5fd2f5;
    --charcoal: #3d3d3f;
    --window-grey: #5c5c5e;
    --window-seam: #48484a;
    --paper: #ffffff;
    --ink: #2f2f31;
  }
  * { box-sizing: border-box; margin: 0; padding: 0; }
  html, body {
    width: 1200px; height: 1200px; overflow: hidden;
    background: var(--backdrop);
  }
  .canvas {
    position: relative; width: 1200px; height: 1200px;
  }
  .panel {
    position: absolute; top: 280px; height: 640px; overflow: hidden;
  }
  .panel-side { left: 136px; width: 384px; }
  .panel-front { left: 520px; width: 544px; background: var(--paper); }
  .panel svg { position: absolute; inset: 0; }

  .side-title {
    position: absolute; left: 112px; top: 0;
    width: 380px; height: 200px;
    transform-origin: 0 0;
    transform: translate(250px, 70px) rotate(90deg);
    font-family: "Orbitron", sans-serif; font-weight: 900;
    font-size: 40px; line-height: 44px; letter-spacing: 1px;
    color: var(--paper); text-transform: uppercase;
  }

  .front-title {
    position: absolute; left: 50px; top: 62px; width: 320px;
    font-family: "Orbitron", sans-serif; font-weight: 900;
    font-size: 21px; line-height: 24px; letter-spacing: 0.5px;
    color: var(--cyan); text-transform: uppercase;
    -webkit-text-stroke: 0.6px #1a9fd0;
  }
  .model-mark {
    position: absolute; right: 44px; top: 52px;
    font-family: "Orbitron", sans-serif; font-weight: 900;
    font-size: 50px; color: var(--ink); letter-spacing: 2px;
  }
  .tech-name {
    position: absolute; left: 50px; top: 128px;
    display: flex; align-items: center; gap: 6px;
    font-family: "Montserrat", sans-serif; font-weight: 700;
    font-size: 17px; color: var(--ink);
  }
  .tech-name .dot {
    width: 14px; height: 14px; border-radius: 50%; background: #1f6fd1;
  }

  .feature-list {
    position: absolute; left: 50px; top: 440px; list-style: none;
    font-family: "Montserrat", sans-serif; font-weight: 300;
    font-size: 19px; line-height: 24px; color: #d8d8da;
  }
  .feature-list b { font-weight: 700; color: var(--paper); }
</style>
</head>
<body>
<div class="canvas">

  <section class="panel panel-side">
    <svg width="384" height="640" viewBox="0 0 384 640">
      <defs>
        <linearGradient id="sideCyan" x1="0" y1="0" x2="1" y2="1">
          <stop offset="0" stop-color="#62d3f6"/>
          <stop offset="1" stop-color="#38b8e6"/>
        </linearGradient>
      </defs>
      <rect width="384" height="640" fill="url(#sideCyan)"/>
      <rect y="380" width="384" height="195" fill="var(--charcoal)"/>
      <rect y="575" width="384" height="65" fill="var(--cyan)"/>
    </svg>
    <div class="side-title">Foldable<br>Airlink<br>Headphone</div>
  </section>

  <section class="panel panel-front">
    <svg width="544" height="640" viewBox="0 0 544 640">
      <rect y="380" width="544" height="195" fill="var(--charcoal)"/>
      <rect y="575" width="544" height="65" fill="var(--cyan)"/>
      <path class="window"
            d="M80,175 H470 Q500,175 500,205 V385 Q500,395 490,401 L375,466 Q360,474 345,466 L250,415 H80 Q50,415 50,385 V205 Q50,175 80,175 Z"
            fill="var(--window-grey)" stroke="var(--paper)" stroke-width="8" stroke-linejoin="round"
            role="img" aria-label="Die-cut window showing the headphones inside"/>
      <line x1="262" y1="179" x2="262" y2="419" stroke="var(--window-seam)" stroke-width="2"/>
    </svg>

    <h1 class="front-title">Foldable Airlink Headphone</h1>
    <div class="model-mark">V5</div>
    <div class="tech-name"><span class="dot"></span>Airlink</div>

    <ul class="feature-list">
      <li>Airlink <b>V5</b></li>
      <li><b>Foldable</b> &amp; Portable</li>
      <li><b>Adjustable</b> headband</li>
      <li>Exceptional Sound <b>Quality</b></li>
      <li><b>Dual Mode</b> wireles or wired connectivity</li>
    </ul>
  </section>

</div>
</body>
</html>
```